Fun A1 2012 family planner using clever typography and block colour

I have been looking for an A1 2012 family planner and I have not been able to find one. Hence I would like help to develop such a planner. I plan to print it on matt paper, portrait orientated. I have attached some reference pictures of our 2011 planner. I like interesting typography, clear clean colours and simple illustration. I need space to write in daily events and need the weeks and days to be clearly delineated from each other. Each day cell needs the date and day in it (please refer to the file uploaded for a visual reference confirming this). Each weekend needs some kind of colour/ typographic delineation. I want a design for a year-at-a-view calendar. I plan to print the planner in Sydney, Australia with brightmarkprinthouse.com.au and probably to sell printed copies online. The terms & conditions of this project are that I will own the design concept 100% and in perpetuity worldwide once payment has been made. (NB. The attached Work File in Word contains a rough layout and all months, days and dates all typed up to make for quicker design.)

Target Market(s)

Reasonably well heeled family of 4. 2 parents. 2 kids. 2 pets.

Industry/Entity Type

Events

Requirements
Must have
• The calendar must be portrait (not landscape orientated), A1 size. It will be printed on matt paper by brightmarkprinthouse.com.au. It must have months running left to right (Jan-Dec) and day/date cells running top to bottom (refer 2011 planner photos in file uploaded). The day/ date cells must be around 3(w)x2(h)cm - big enough to write daily events in. Weekends must be colour/ typographically delineated. 2012 year must be noted as must "A Paperkite Inc Project" and web address in fine print bottom left hand left hand corner.
Nice to have
• A Paperkite Inc logo in bottom left hand corder (perhaps Merry Otter like: http://www.pixelvault-example.com/design_submission.aspx?designid=731604). Header/Footer space for customisation (e.g. "Brandt-Osei 2012 Planner" or "QRN Co 2012 Planner".
Should not have
• The calendar should not use photographs or resemble standard or cheesy wall calendars. No watermarks please.

```html
<!DOCTYPE html>
<html lang="en">
<head>
<meta charset="utf-8">
<title>A Paperkite Inc 2012 Planner</title>
<link href="https://fonts.googleapis.com/css2?family=Bree+Serif&family=Alegreya:wght@400;700&family=Cabin:wght@500&display=swap" rel="stylesheet">
<style>
:root{
  --green:#8cc63f;
  --orange:#f47b20;
  --purple:#6a2c91;
  --peach:#fdd9bd;
  --ink:#2a1a33;
  --rule:#c9b6dc;
  --divider:#e6e0b8;
  --paper:#ffffff;
  --backdrop:#ffffff;
}
*{box-sizing:border-box;margin:0;padding:0}
html,body{width:1200px;height:900px;overflow:hidden;background:var(--backdrop)}
.planner{position:absolute;left:287px;top:2px;width:626px;height:896px;background:var(--paper);border:1px solid var(--rule)}
.masthead{position:absolute;left:0;top:0;width:100%;height:64px}
.artwork{position:absolute;left:18px;top:8px;width:400px;height:46px;border-radius:10px;background:linear-gradient(90deg,var(--green),#a6d46a)}
.year{position:absolute;right:6px;top:-12px;font-family:"Bree Serif",serif;font-weight:400;font-size:74px;color:var(--green);letter-spacing:-1px;line-height:1}
.months{position:absolute;left:5px;top:64px;width:616px;height:14px;background:var(--orange);display:grid;grid-template-columns:repeat(12,1fr)}
.months span{font-family:"Bree Serif",serif;font-size:9px;color:var(--green);text-align:center;line-height:14px}
.grid{position:absolute;left:5px;top:78px;width:616px;height:763px;display:grid;grid-template-columns:repeat(12,1fr)}
.month{list-style:none;display:grid;grid-template-rows:repeat(31,24.6px);border-right:1px solid var(--divider)}
.month--tint{background:var(--peach)}
.month li{font-family:"Alegreya",serif;font-size:7px;color:var(--ink);line-height:9px;padding:0 2px;white-space:nowrap;overflow:hidden}
.month li b{font-weight:700}
.month li i{font-style:normal;color:var(--orange)}
.month li.we{background:linear-gradient(var(--purple),var(--purple)) top/100% 9px no-repeat;color:#fff}
.footer{position:absolute;left:5px;right:5px;bottom:6px;display:flex;justify-content:space-between;align-items:baseline}
.credit{font-family:"Cabin",sans-serif;font-size:19px;color:var(--green)}
.web{font-family:"Bree Serif",serif;font-size:19px;color:var(--orange)}
</style>
</head>
<body>
<main class="planner">
  <header class="masthead">
    <div class="artwork" role="img" aria-label="Illustration of a family's shoes walking across the top of the planner"></div>
    <h1 class="year">2012</h1>
  </header>

  <div class="months">
    <span>january</span><span>february</span><span>march</span><span>april</span><span>may</span><span>june</span><span>july</span><span>august</span><span>september</span><span>october</span><span>november</span><span>december</span>
  </div>

  <section class="grid">
    <ul class="month month--tint">
      <li class="we"><b>1</b> sunday</li><li><b>2</b> mon<i>day</i></li><li><b>3</b> tues<i>day</i></li><li><b>4</b> wednes<i>day</i></li><li><b>5</b> thurs<i>day</i></li><li><b>6</b> fri<i>day</i></li><li class="we"><b>7</b> saturday</li>
      <li class="we"><b>8</b> sunday</li><li><b>9</b> mon<i>day</i></li><li><b>10</b> tues<i>day</i></li><li><b>11</b> wednes<i>day</i></li><li><b>12</b> thurs<i>day</i></li><li><b>13</b> fri<i>day</i></li><li class="we"><b>14</b> saturday</li>
      <li class="we"><b>15</b> sunday</li><li><b>16</b> mon<i>day</i></li><li><b>17</b> tues<i>day</i></li><li><b>18</b> wednes<i>day</i></li><li><b>19</b> thurs<i>day</i></li><li><b>20</b> fri<i>day</i></li><li class="we"><b>21</b> saturday</li>
      <li class="we"><b>22</b> sunday</li><li><b>23</b> mon<i>day</i></li><li><b>24</b> tues<i>day</i></li><li><b>25</b> wednes<i>day</i></li><li><b>26</b> thurs<i>day</i></li><li><b>27</b> fri<i>day</i></li><li class="we"><b>28</b> saturday</li>
      <li class="we"><b>29</b> sunday</li><li><b>30</b> mon<i>day</i></li><li><b>31</b> tues<i>day</i></li>
    </ul>
    <ul class="month">
      <li><b>1</b> wednes<i>day</i></li><li><b>2</b> thurs<i>day</i></li><li><b>3</b> fri<i>day</i></li><li class="we"><b>4</b> saturday</li><li class="we"><b>5</b> sunday</li><li><b>6</b> mon<i>day</i></li><li><b>7</b> tues<i>day</i></li>
      <li><b>8</b> wednes<i>day</i></li><li><b>9</b> thurs<i>day</i></li><li><b>10</b> fri<i>day</i></li><li class="we"><b>11</b> saturday</li><li class="we"><b>12</b> sunday</li><li><b>13</b> mon<i>day</i></li><li><b>14</b> tues<i>day</i></li>
      <li><b>15</b> wednes<i>day</i></li><li><b>16</b> thurs<i>day</i></li><li><b>17</b> fri<i>day</i></li><li class="we"><b>18</b> saturday</li><li class="we"><b>19</b> sunday</li><li><b>20</b> mon<i>day</i></li><li><b>21</b> tues<i>day</i></li>
      <li><b>22</b> wednes<i>day</i></li><li><b>23</b> thurs<i>day</i></li><li><b>24</b> fri<i>day</i></li><li class="we"><b>25</b> saturday</li><li class="we"><b>26</b> sunday</li><li><b>27</b> mon<i>day</i></li><li><b>28</b> tues<i>day</i></li>
      <li><b>29</b> wednes<i>day</i></li>
    </ul>
    <ul class="month month--tint">
      <li><b>1</b> thurs<i>day</i></li><li><b>2</b> fri<i>day</i></li><li class="we"><b>3</b> saturday</li><li class="we"><b>4</b> sunday</li><li><b>5</b> mon<i>day</i></li><li><b>6</b> tues<i>day</i></li><li><b>7</b> wednes<i>day</i></li>
      <li><b>8</b> thurs<i>day</i></li><li><b>9</b> fri<i>day</i></li><li class="we"><b>10</b> saturday</li><li class="we"><b>11</b> sunday</li><li><b>12</b> mon<i>day</i></li><li><b>13</b> tues<i>day</i></li><li><b>14</b> wednes<i>day</i></li>
      <li><b>15</b> thurs<i>day</i></li><li><b>16</b> fri<i>day</i></li><li class="we"><b>17</b> saturday</li><li class="we"><b>18</b> sunday</li><li><b>19</b> mon<i>day</i></li><li><b>20</b> tues<i>day</i></li><li><b>21</b> wednes<i>day</i></li>
      <li><b>22</b> thurs<i>day</i></li><li><b>23</b> fri<i>day</i></li><li class="we"><b>24</b> saturday</li><li class="we"><b>25</b> sunday</li><li><b>26</b> mon<i>day</i></li><li><b>27</b> tues<i>day</i></li><li><b>28</b> wednes<i>day</i></li>
      <li><b>29</b> thurs<i>day</i></li><li><b>30</b> fri<i>day</i></li><li class="we"><b>31</b> saturday</li>
    </ul>
    <ul class="month">
      <li class="we"><b>1</b> sunday</li><li><b>2</b> mon<i>day</i></li><li><b>3</b> tues<i>day</i></li><li><b>4</b> wednes<i>day</i></li><li><b>5</b> thurs<i>day</i></li><li><b>6</b> fri<i>day</i></li><li class="we"><b>7</b> saturday</li>
      <li class="we"><b>8</b> sunday</li><li><b>9</b> mon<i>day</i></li><li><b>10</b> tues<i>day</i></li><li><b>11</b> wednes<i>day</i></li><li><b>12</b> thurs<i>day</i></li><li><b>13</b> fri<i>day</i></li><li class="we"><b>14</b> saturday</li>
      <li class="we"><b>15</b> sunday</li><li><b>16</b> mon<i>day</i></li><li><b>17</b> tues<i>day</i></li><li><b>18</b> wednes<i>day</i></li><li><b>19</b> thurs<i>day</i></li><li><b>20</b> fri<i>day</i></li><li class="we"><b>21</b> saturday</li>
      <li class="we"><b>22</b> sunday</li><li><b>23</b> mon<i>day</i></li><li><b>24</b> tues<i>day</i></li><li><b>25</b> wednes<i>day</i></li><li><b>26</b> thurs<i>day</i></li><li><b>27</b> fri<i>day</i></li><li class="we"><b>28</b> saturday</li>
      <li class="we"><b>29</b> sunday</li><li><b>30</b> mon<i>day</i></li>
    </ul>
    <ul class="month month--tint">
      <li><b>1</b> tues<i>day</i></li><li><b>2</b> wednes<i>day</i></li><li><b>3</b> thurs<i>day</i></li><li><b>4</b> fri<i>day</i></li><li class="we"><b>5</b> saturday</li><li class="we"><b>6</b> sunday</li><li><b>7</b> mon<i>day</i></li>
      <li><b>8</b> tues<i>day</i></li><li><b>9</b> wednes<i>day</i></li><li><b>10</b> thurs<i>day</i></li><li><b>11</b> fri<i>day</i></li><li class="we"><b>12</b> saturday</li><li class="we"><b>13</b> sunday</li><li><b>14</b> mon<i>day</i></li>
      <li><b>15</b> tues<i>day</i></li><li><b>16</b> wednes<i>day</i></li><li><b>17</b> thurs<i>day</i></li><li><b>18</b> fri<i>day</i></li><li class="we"><b>19</b> saturday</li><li class="we"><b>20</b> sunday</li><li><b>21</b> mon<i>day</i></li>
      <li><b>22</b> tues<i>day</i></li><li><b>23</b> wednes<i>day</i></li><li><b>24</b> thurs<i>day</i></li><li><b>25</b> fri<i>day</i></li><li class="we"><b>26</b> saturday</li><li class="we"><b>27</b> sunday</li><li><b>28</b> mon<i>day</i></li>
      <li><b>29</b> tues<i>day</i></li><li><b>30</b> wednes<i>day</i></li><li><b>31</b> thurs<i>day</i></li>
    </ul>
    <ul class="month">
      <li><b>1</b> fri<i>day</i></li><li class="we"><b>2</b> saturday</li><li class="we"><b>3</b> sunday</li><li><b>4</b> mon<i>day</i></li><li><b>5</b> tues<i>day</i></li><li><b>6</b> wednes<i>day</i></li><li><b>7</b> thurs<i>day</i></li>
      <li><b>8</b> fri<i>day</i></li><li class="we"><b>9</b> saturday</li><li class="we"><b>10</b> sunday</li><li><b>11</b> mon<i>day</i></li><li><b>12</b> tues<i>day</i></li><li><b>13</b> wednes<i>day</i></li><li><b>14</b> thurs<i>day</i></li>
      <li><b>15</b> fri<i>day</i></li><li class="we"><b>16</b> saturday</li><li class="we"><b>17</b> sunday</li><li><b>18</b> mon<i>day</i></li><li><b>19</b> tues<i>day</i></li><li><b>20</b> wednes<i>day</i></li><li><b>21</b> thurs<i>day</i></li>
      <li><b>22</b> fri<i>day</i></li><li class="we"><b>23</b> saturday</li><li class="we"><b>24</b> sunday</li><li><b>25</b> mon<i>day</i></li><li><b>26</b> tues<i>day</i></li><li><b>27</b> wednes<i>day</i></li><li><b>28</b> thurs<i>day</i></li>
      <li><b>29</b> fri<i>day</i></li><li class="we"><b>30</b> saturday</li>
    </ul>
    <ul class="month month--tint">
      <li class="we"><b>1</b> sunday</li><li><b>2</b> mon<i>day</i></li><li><b>3</b> tues<i>day</i></li><li><b>4</b> wednes<i>day</i></li><li><b>5</b> thurs<i>day</i></li><li><b>6</b> fri<i>day</i></li><li class="we"><b>7</b> saturday</li>
      <li class="we"><b>8</b> sunday</li><li><b>9</b> mon<i>day</i></li><li><b>10</b> tues<i>day</i></li><li><b>11</b> wednes<i>day</i></li><li><b>12</b> thurs<i>day</i></li><li><b>13</b> fri<i>day</i></li><li class="we"><b>14</b> saturday</li>
      <li class="we"><b>15</b> sunday</li><li><b>16</b> mon<i>day</i></li><li><b>17</b> tues<i>day</i></li><li><b>18</b> wednes<i>day</i></li><li><b>19</b> thurs<i>day</i></li><li><b>20</b> fri<i>day</i></li><li class="we"><b>21</b> saturday</li>
      <li class="we"><b>22</b> sunday</li><li><b>23</b> mon<i>day</i></li><li><b>24</b> tues<i>day</i></li><li><b>25</b> wednes<i>day</i></li><li><b>26</b> thurs<i>day</i></li><li><b>27</b> fri<i>day</i></li><li class="we"><b>28</b> saturday</li>
      <li class="we"><b>29</b> sunday</li><li><b>30</b> mon<i>day</i></li><li><b>31</b> tues<i>day</i></li>
    </ul>
    <ul class="month">
      <li><b>1</b> wednes<i>day</i></li><li><b>2</b> thurs<i>day</i></li><li><b>3</b> fri<i>day</i></li><li class="we"><b>4</b> saturday</li><li class="we"><b>5</b> sunday</li><li><b>6</b> mon<i>day</i></li><li><b>7</b> tues<i>day</i></li>
      <li><b>8</b> wednes<i>day</i></li><li><b>9</b> thurs<i>day</i></li><li><b>10</b> fri<i>day</i></li><li class="we"><b>11</b> saturday</li><li class="we"><b>12</b> sunday</li><li><b>13</b> mon<i>day</i></li><li><b>14</b> tues<i>day</i></li>
      <li><b>15</b> wednes<i>day</i></li><li><b>16</b> thurs<i>day</i></li><li><b>17</b> fri<i>day</i></li><li class="we"><b>18</b> saturday</li><li class="we"><b>19</b> sunday</li><li><b>20</b> mon<i>day</i></li><li><b>21</b> tues<i>day</i></li>
      <li><b>22</b> wednes<i>day</i></li><li><b>23</b> thurs<i>day</i></li><li><b>24</b> fri<i>day</i></li><li class="we"><b>25</b> saturday</li><li class="we"><b>26</b> sunday</li><li><b>27</b> mon<i>day</i></li><li><b>28</b> tues<i>day</i></li>
      <li><b>29</b> wednes<i>day</i></li><li><b>30</b> thurs<i>day</i></li><li><b>31</b> fri<i>day</i></li>
    </ul>
    <ul class="month month--tint">
      <li class="we"><b>1</b> saturday</li><li class="we"><b>2</b> sunday</li><li><b>3</b> mon<i>day</i></li><li><b>4</b> tues<i>day</i></li><li><b>5</b> wednes<i>day</i></li><li><b>6</b> thurs<i>day</i></li><li><b>7</b> fri<i>day</i></li>
      <li class="we"><b>8</b> saturday</li><li class="we"><b>9</b> sunday</li><li><b>10</b> mon<i>day</i></li><li><b>11</b> tues<i>day</i></li><li><b>12</b> wednes<i>day</i></li><li><b>13</b> thurs<i>day</i></li><li><b>14</b> fri<i>day</i></li>
      <li class="we"><b>15</b> saturday</li><li class="we"><b>16</b> sunday</li><li><b>17</b> mon<i>day</i></li><li><b>18</b> tues<i>day</i></li><li><b>19</b> wednes<i>day</i></li><li><b>20</b> thurs<i>day</i></li><li><b>21</b> fri<i>day</i></li>
      <li class="we"><b>22</b> saturday</li><li class="we"><b>23</b> sunday</li><li><b>24</b> mon<i>day</i></li><li><b>25</b> tues<i>day</i></li><li><b>26</b> wednes<i>day</i></li><li><b>27</b> thurs<i>day</i></li><li><b>28</b> fri<i>day</i></li>
      <li class="we"><b>29</b> saturday</li><li class="we"><b>30</b> sunday</li>
    </ul>
    <ul class="month">
      <li><b>1</b> mon<i>day</i></li><li><b>2</b> tues<i>day</i></li><li><b>3</b> wednes<i>day</i></li><li><b>4</b> thurs<i>day</i></li><li><b>5</b> fri<i>day</i></li><li class="we"><b>6</b> saturday</li><li class="we"><b>7</b> sunday</li>
      <li><b>8</b> mon<i>day</i></li><li><b>9</b> tues<i>day</i></li><li><b>10</b> wednes<i>day</i></li><li><b>11</b> thurs<i>day</i></li><li><b>12</b> fri<i>day</i></li><li class="we"><b>13</b> saturday</li><li class="we"><b>14</b> sunday</li>
      <li><b>15</b> mon<i>day</i></li><li><b>16</b> tues<i>day</i></li><li><b>17</b> wednes<i>day</i></li><li><b>18</b> thurs<i>day</i></li><li><b>19</b> fri<i>day</i></li><li class="we"><b>20</b> saturday</li><li class="we"><b>21</b> sunday</li>
      <li><b>22</b> mon<i>day</i></li><li><b>23</b> tues<i>day</i></li><li><b>24</b> wednes<i>day</i></li><li><b>25</b> thurs<i>day</i></li><li><b>26</b> fri<i>day</i></li><li class="we"><b>27</b> saturday</li><li class="we"><b>28</b> sunday</li>
      <li><b>29</b> mon<i>day</i></li><li><b>30</b> tues<i>day</i></li><li><b>31</b> wednes<i>day</i></li>
    </ul>
    <ul class="month month--tint">
      <li><b>1</b> thurs<i>day</i></li><li><b>2</b> fri<i>day</i></li><li class="we"><b>3</b> saturday</li><li class="we"><b>4</b> sunday</li><li><b>5</b> mon<i>day</i></li><li><b>6</b> tues<i>day</i></li><li><b>7</b> wednes<i>day</i></li>
      <li><b>8</b> thurs<i>day</i></li><li><b>9</b> fri<i>day</i></li><li class="we"><b>10</b> saturday</li><li class="we"><b>11</b> sunday</li><li><b>12</b> mon<i>day</i></li><li><b>13</b> tues<i>day</i></li><li><b>14</b> wednes<i>day</i></li>
      <li><b>15</b> thurs<i>day</i></li><li><b>16</b> fri<i>day</i></li><li class="we"><b>17</b> saturday</li><li class="we"><b>18</b> sunday</li><li><b>19</b> mon<i>day</i></li><li><b>20</b> tues<i>day</i></li><li><b>21</b> wednes<i>day</i></li>
      <li><b>22</b> thurs<i>day</i></li><li><b>23</b> fri<i>day</i></li><li class="we"><b>24</b> saturday</li><li class="we"><b>25</b> sunday</li><li><b>26</b> mon<i>day</i></li><li><b>27</b> tues<i>day</i></li><li><b>28</b> wednes<i>day</i></li>
      <li><b>29</b> thurs<i>day</i></li><li><b>30</b> fri<i>day</i></li>
    </ul>
    <ul class="month">
      <li class="we"><b>1</b> saturday</li><li class="we"><b>2</b> sunday</li><li><b>3</b> mon<i>day</i></li><li><b>4</b> tues<i>day</i></li><li><b>5</b> wednes<i>day</i></li><li><b>6</b> thurs<i>day</i></li><li><b>7</b> fri<i>day</i></li>
      <li class="we"><b>8</b> saturday</li><li class="we"><b>9</b> sunday</li><li><b>10</b> mon<i>day</i></li><li><b>11</b> tues<i>day</i></li><li><b>12</b> wednes<i>day</i></li><li><b>13</b> thurs<i>day</i></li><li><b>14</b> fri<i>day</i></li>
      <li class="we"><b>15</b> saturday</li><li class="we"><b>16</b> sunday</li><li><b>17</b> mon<i>day</i></li><li><b>18</b> tues<i>day</i></li><li><b>19</b> wednes<i>day</i></li><li><b>20</b> thurs<i>day</i></li><li><b>21</b> fri<i>day</i></li>
      <li class="we"><b>22</b> saturday</li><li class="we"><b>23</b> sunday</li><li><b>24</b> mon<i>day</i></li><li><b>25</b> tues<i>day</i></li><li><b>26</b> wednes<i>day</i></li><li><b>27</b> thurs<i>day</i></li><li><b>28</b> fri<i>day</i></li>
      <li class="we"><b>29</b> saturday</li><li class="we"><b>30</b> sunday</li><li><b>31</b> mon<i>day</i></li>
    </ul>
  </section>

  <footer class="footer">
    <span class="credit">A Paperkite Inc Project</span>
    <span class="web">www.paperkiteplanner.com</span>
  </footer>
</main>
</body>
</html>
```